Book cover for a feel-good story

Creation of a cover for the book: "A lantern on a window sill"

Title: "A lantern on a windowsill" (The English translation should not appear)
Author: "Margaux Dubrac"
Publisher: "Editions Corvelle" (should be at the bottom of the page)
Format: 14 x 20.5 cm

The story :
A young single woman (32 years old) is a blogger, she has a passion for shoes.
She has pink hair, just because she likes it. She loves flowers

The text is a humorous story of the woman and the relationship with her mother, similar to Harriet Pemble stories.
A feel good text +++

(The words "diamond" and "shoe box" are not keyword, they do not call for representation in the image. They are just a citation from the book)

Enclosed (joined files): examples of styles' cover that would have suited.

Teenagers, young adults

Book

• shoes, pink hair, flowers
• Diamond, box of shoes

```html
<!DOCTYPE html>
<html lang="fr">
<head>
<meta charset="utf-8">
<title>Une Lanterne sur le rebord de fenêtre — Margaux Dubrac</title>
<link rel="stylesheet" href="https://fonts.googleapis.com/css2?family=Dancing+Script:wght@600&family=Poppins:wght@500;600&display=swap">
<style>
  :root {
    --page: #ffffff;
    --cover-top: #ecb8b1;
    --cover-bottom: #e8a9a4;
    --title: #ffffff;
    --ink: #2d2846;
    --figure-light: #f2f0ef;
    --figure-coral: #e0634c;
    --figure-navy: #2f2c4c;
    --blossom: #f7dcdc;
  }
  * { box-sizing: border-box; margin: 0; padding: 0; }
  html, body {
    width: 1200px;
    height: 939px;
    overflow: hidden;
    background: var(--page);
  }
  .book-cover {
    position: absolute;
    left: 370px;
    top: 94px;
    width: 460px;
    height: 752px;
    background: linear-gradient(180deg, var(--cover-top), var(--cover-bottom));
    overflow: hidden;
  }
  .cover-illustration {
    position: absolute;
    left: 0;
    top: 0;
    width: 300px;
    height: 592px;
    background: linear-gradient(180deg,
      var(--figure-light) 0%,
      var(--figure-light) 30%,
      var(--figure-coral) 42%,
      var(--figure-coral) 82%,
      var(--figure-navy) 100%);
    border-radius: 0 60px 40px 0;
    opacity: 0.9;
  }
  .blossom-cluster {
    position: absolute;
    left: 256px;
    top: 286px;
    width: 92px;
    height: 88px;
    border-radius: 50%;
    background: radial-gradient(circle, var(--blossom), transparent 70%);
  }
  .book-title {
    position: absolute;
    left: 150px;
    top: 70px;
    width: 290px;
    color: var(--title);
    font-family: "Dancing Script", cursive;
    font-weight: 600;
    line-height: 1;
  }
  .title-article {
    display: block;
    font-size: 30px;
    margin-left: 118px;
  }
  .title-main {
    display: block;
    font-size: 76px;
    margin-top: -6px;
  }
  .title-middle {
    display: flex;
    align-items: center;
    gap: 8px;
    margin-left: 30px;
    margin-top: 2px;
  }
  .title-small {
    display: flex;
    flex-direction: column;
    font-size: 22px;
    line-height: 0.9;
  }
  .title-mid {
    font-size: 42px;
  }
  .title-last {
    display: block;
    font-size: 46px;
    margin-left: 74px;
    margin-top: 0;
  }
  .book-author {
    position: absolute;
    left: 0;
    right: 0;
    top: 604px;
    text-align: center;
    padding-left: 36px;
    color: var(--ink);
    font-family: "Poppins", sans-serif;
    font-weight: 600;
    font-size: 32px;
    letter-spacing: 6px;
    text-transform: uppercase;
  }
  .book-publisher {
    position: absolute;
    left: 0;
    right: 0;
    top: 684px;
    text-align: center;
    color: var(--ink);
    font-family: "Poppins", sans-serif;
    font-weight: 500;
    font-size: 19px;
  }
</style>
</head>
<body>
  <main class="book-cover">
    <div class="cover-illustration" role="img" aria-label="Illustration d'une jeune femme en collants corail et baskets bleu marine d'où sortent des fleurs"></div>
    <div class="blossom-cluster" role="img" aria-label="Fleurs de cerisier roses et blanches"></div>

    <h1 class="book-title">
      <span class="title-article">Une</span>
      <span class="title-main">Lanterne</span>
      <span class="title-middle">
        <span class="title-small"><span>sur</span><span>le</span></span>
        <span class="title-mid">rebord de</span>
      </span>
      <span class="title-last">fenêtre</span>
    </h1>

    <p class="book-author">Margaux Dubrac</p>
    <p class="book-publisher">Editions Corvelle</p>
  </main>
</body>
</html>
```